Business Card for a Wedding Films Business

We require a business card design for our business 'Lewis Marrow Wedding Films'. The logo needs to look classy and high end.

Target Market(s)

Wedding Couples

Contact Information for Business Card

Lewis Marrow Wedding Films
07312 605 227
films@lewismarrowreels.com
www.lewismarrowreels.com

Facebook: @lewismarrowweddingfilms
Instagram: @lewismarrowfilms

Font styles to use
Sans Serif

Requirements
Must have
• Social media icons - Facebook and Instagram

```html
<!DOCTYPE html>
<html lang="en">
<head>
<meta charset="utf-8">
<title>Lewis Marrow Wedding Films – Business Card</title>
<link rel="stylesheet" href="https://fonts.googleapis.com/css2?family=Josefin+Sans:wght@600&family=Montserrat:wght@700&family=Roboto:wght@300;400&display=swap">
<style>
  :root {
    --backdrop: #2a2a2b;
    --card: #1f1f20;
    --gold: #d9a93f;
    --gold-light: #f6de85;
    --gold-deep: #c8861f;
    --gold-text: #e0b24c;
  }
  * { margin: 0; padding: 0; box-sizing: border-box; }
  html, body { width: 1200px; height: 901px; overflow: hidden; background: var(--backdrop); }
  .canvas {
    position: relative; width: 1200px; height: 901px;
    display: flex; flex-direction: column; align-items: center; justify-content: center; gap: 22px;
  }
  .card {
    position: relative; width: 720px; height: 411px;
    background: var(--card);
    box-shadow: 0 10px 30px rgba(0,0,0,.45);
    overflow: hidden;
  }
  .gold-band {
    position: absolute; left: 0; right: 0; bottom: 0; height: 9px;
    background: linear-gradient(90deg, var(--gold) 0%, var(--gold-light) 22%, var(--gold-deep) 50%, var(--gold-light) 78%, var(--gold) 100%);
  }
  .wordmark {
    font-family: "Josefin Sans", sans-serif; font-weight: 600;
    color: var(--gold-text); text-transform: uppercase; text-align: center; line-height: 1;
  }
  .wordmark .primary { display: block; }
  .wordmark .secondary { display: block; }

  /* front */
  .card-front .wordmark {
    position: absolute; left: 0; right: 0; top: 160px;
  }
  .card-front .primary { font-size: 40px; letter-spacing: 10px; }
  .card-front .secondary { font-size: 17px; letter-spacing: 9px; margin-top: 14px; }

  /* back */
  .card-back .wordmark {
    position: absolute; left: 40px; width: 300px; top: 150px;
  }
  .card-back .primary { font-size: 25px; letter-spacing: 6px; }
  .card-back .secondary { font-size: 11px; letter-spacing: 6px; margin-top: 10px; }
  .divider {
    position: absolute; left: 362px; top: 95px; width: 2px; height: 170px;
    background: var(--gold);
  }
  .contact { position: absolute; left: 392px; top: 105px; color: var(--gold-text); font-family: Roboto, sans-serif; }
  .contact .name { font-family: Montserrat, sans-serif; font-weight: 700; font-size: 25px; color: var(--gold-light); }
  .contact .role { font-weight: 300; font-size: 18px; margin-top: 2px; margin-bottom: 22px; }
  .contact-row { display: flex; align-items: center; gap: 12px; font-size: 19px; font-weight: 400; margin-bottom: 8px; }
  .contact-row svg { width: 17px; height: 17px; flex: none; }
  .socials {
    position: absolute; left: 0; right: 0; bottom: 40px;
    display: flex; justify-content: center; gap: 30px;
    font-family: Roboto, sans-serif; font-size: 19px; color: var(--gold-text);
  }
  .social { display: flex; align-items: center; gap: 9px; }
  .social .dot { width: 17px; height: 17px; border: 2px solid var(--gold-text); border-radius: 50%; }
</style>
</head>
<body>
<main class="canvas">
  <section class="card card-front">
    <div class="wordmark">
      <span class="primary">Lewis Marrow</span>
      <span class="secondary">Wedding Films</span>
    </div>
    <div class="gold-band"></div>
  </section>

  <section class="card card-back">
    <div class="wordmark">
      <span class="primary">Lewis Marrow</span>
      <span class="secondary">Wedding Films</span>
    </div>
    <div class="divider"></div>
    <div class="contact">
      <div class="name">Lewis Marrow</div>
      <div class="role">Wedding Films</div>
      <div class="contact-row">
        <svg viewBox="0 0 24 24" fill="none" stroke="currentColor" stroke-width="2"><path d="M5 3h4l2 5-2.5 1.5a11 11 0 0 0 6 6L16 13l5 2v4a2 2 0 0 1-2 2A16 16 0 0 1 3 5a2 2 0 0 1 2-2z"/></svg>
        <span>07312 605 227</span>
      </div>
      <div class="contact-row">
        <svg viewBox="0 0 24 24" fill="none" stroke="currentColor" stroke-width="2"><rect x="3" y="5" width="18" height="14" rx="1"/><path d="M3 6l9 7 9-7"/></svg>
        <span>films@lewismarrowreels.com</span>
      </div>
      <div class="contact-row">
        <svg viewBox="0 0 24 24" fill="none" stroke="currentColor" stroke-width="2"><circle cx="12" cy="12" r="9"/><path d="M3 12h18M12 3c3 3 3 15 0 18M12 3c-3 3-3 15 0 18"/></svg>
        <span>www.lewismarrowreels.com</span>
      </div>
    </div>
    <div class="socials">
      <div class="social"><span class="dot"></span><span>@lewismarrowweddingfilms</span></div>
      <div class="social"><span class="dot"></span><span>@lewismarrowfilms</span></div>
    </div>
    <div class="gold-band"></div>
  </section>
</main>
</body>
</html>
```